Plume & Crest Hair Extensions needs a business card

We need a business card designed for an online luxury hair extensions business called Plume & Crest, we already have a logo and need an innovative business card (2-sided preferably). The strap line for the brand is 'Luxury Hair At Every Touchpoint!'. The brand is a premium brand selling virgin hair extensions and the target market is the mid-affluent ethnic woman as such the design should reflect this. The brand logo is grey and can be sent when requested.

Target Market(s)

25 to 35 year mid-affluent ethnic woman (Afro-American, Mixed Race, Asian)

Industry/Entity Type

Hair

Colors

Designer to choose colors to be used in the design.

Requirements
Must have
• Business Name: Plume and Crest
Strapline: Luxury hair at every touchpoint!
Domain: ​www.plumeandcrest.example
Email: info@plumeandcrest.example
sales and enquiries
44 07500 xxxxxxx

Please use the grey main brand logo depicted in page 2 of the attached pdf document

```html
<!DOCTYPE html>
<html lang="en">
<head>
<meta charset="utf-8">
<title>Plume &amp; Crest Hair Extensions – Business Card</title>
<link rel="stylesheet" href="https://fonts.googleapis.com/css2?family=Great+Vibes&family=Montserrat:wght@400;600&display=swap">
<style>
  :root {
    --backdrop: #ede6df;
    --copper-light: #f2c9a6;
    --copper-mid: #d9895a;
    --copper-deep: #b0653a;
    --brand-grey: #a9a9ab;
    --ink: #2a1a12;
    --band: #1d1c1c;
    --icon: #7a4a30;
    --photo-hair: #8a5a34;
    --photo-skin: #e6bfa0;
  }
  * { box-sizing: border-box; margin: 0; padding: 0; }
  html, body { width: 1200px; height: 902px; overflow: hidden; }
  body {
    background: var(--backdrop);
    font-family: "Montserrat", Arial, sans-serif;
    position: relative;
  }
  .card {
    position: absolute;
    left: 320px;
    width: 560px;
    height: 320px;
    border-radius: 4px;
    overflow: hidden;
    box-shadow: 0 10px 28px rgba(60, 35, 20, 0.25);
  }
  .card--front {
    top: 110px;
    background: linear-gradient(200deg, var(--copper-deep) 0%, var(--copper-mid) 35%, var(--copper-light) 100%);
  }
  .card--back {
    top: 472px;
    background: linear-gradient(200deg, var(--copper-mid) 0%, var(--copper-light) 70%, #f6dcc6 100%);
  }

  /* Brand name block (front) */
  .brand {
    position: absolute;
    display: flex;
    align-items: center;
    gap: 14px;
  }
  .brand__dot {
    border-radius: 50%;
    background: var(--brand-grey);
  }
  .brand__name {
    color: var(--brand-grey);
    font-weight: 600;
    text-transform: uppercase;
    letter-spacing: 0.08em;
    white-space: nowrap;
  }
  .card--front .brand { left: 80px; top: 128px; }
  .card--front .brand__dot { width: 34px; height: 34px; }
  .card--front .brand__name { font-size: 38px; }

  .tagline {
    position: absolute;
    font-family: "Great Vibes", cursive;
    color: var(--ink);
    white-space: nowrap;
  }
  .card--front .tagline { left: 128px; top: 190px; font-size: 31px; }

  /* Back */
  .portrait {
    position: absolute;
    right: 0;
    top: 0;
    width: 280px;
    height: 200px;
    background: radial-gradient(ellipse at 45% 45%, var(--photo-skin) 0%, var(--photo-hair) 55%, rgba(176, 101, 58, 0) 100%);
  }
  .band {
    position: absolute;
    left: 0;
    right: 0;
    bottom: 0;
    height: 46px;
    background: var(--band);
  }
  .card--back .brand { left: 28px; top: 160px; gap: 8px; }
  .card--back .brand__dot { width: 16px; height: 16px; }
  .card--back .brand__name { font-size: 17px; }
  .card--back .tagline { left: 40px; top: 190px; font-size: 16px; }

  .contacts {
    position: absolute;
    left: 240px;
    top: 142px;
    list-style: none;
  }
  .contacts__item {
    display: flex;
    align-items: center;
    gap: 10px;
    height: 30px;
    font-size: 15px;
    color: var(--ink);
  }
  .contacts__icon {
    width: 18px;
    height: 18px;
    flex: none;
  }
  .contacts__spacer { width: 18px; flex: none; }
</style>
</head>
<body>

<section class="card card--front" aria-label="Business card front">
  <div class="brand">
    <span class="brand__dot"></span>
    <span class="brand__name">Plume &amp; Crest</span>
  </div>
  <p class="tagline">Luxury hair at every touchpoint!</p>
</section>

<section class="card card--back" aria-label="Business card back">
  <div class="portrait" role="img" aria-label="Portrait photograph of a model with long flowing brown hair"></div>

  <div class="brand">
    <span class="brand__dot"></span>
    <span class="brand__name">Plume &amp; Crest</span>
  </div>
  <p class="tagline">Luxury hair at every touchpoint!</p>

  <ul class="contacts">
    <li class="contacts__item">
      <svg class="contacts__icon" viewBox="0 0 20 20" aria-hidden="true">
        <circle cx="10" cy="10" r="9" fill="var(--icon)"/>
        <g fill="none" stroke="#f3d7c2" stroke-width="1.2">
          <circle cx="10" cy="10" r="5.5"/>
          <ellipse cx="10" cy="10" rx="2.4" ry="5.5"/>
          <line x1="4.5" y1="10" x2="15.5" y2="10"/>
        </g>
      </svg>
      <span>www.plumeandcrest.example</span>
    </li>
    <li class="contacts__item">
      <svg class="contacts__icon" viewBox="0 0 20 20" aria-hidden="true">
        <circle cx="10" cy="10" r="9" fill="var(--icon)"/>
        <rect x="5" y="6.5" width="10" height="7" fill="none" stroke="#f3d7c2" stroke-width="1.2"/>
        <polyline points="5,6.5 10,10.5 15,6.5" fill="none" stroke="#f3d7c2" stroke-width="1.2"/>
      </svg>
      <span>info@plumeandcrest.example</span>
    </li>
    <li class="contacts__item">
      <span class="contacts__spacer"></span>
      <span>Sales &amp; Enquiry</span>
    </li>
    <li class="contacts__item">
      <svg class="contacts__icon" viewBox="0 0 20 20" aria-hidden="true">
        <circle cx="10" cy="10" r="9" fill="var(--icon)"/>
        <path d="M7 5.5 L8.8 5.5 L9.4 8 L8.3 8.9 Q9.3 11 11.1 11.8 L12 10.7 L14.5 11.3 L14.5 13.1 Q10.5 14 8 11.5 Q5.8 9.2 7 5.5 Z" fill="#f3d7c2"/>
      </svg>
      <span>44 07500 xxxxxxx</span>
    </li>
  </ul>

  <div class="band"></div>
</section>

</body>
</html>
```